Real Estate Company Needs Business Card Designed

We need a business card design for a new real estate company based in Campbell, CA (Silicon Valley). We plan to improve the residential real estate industry by using technology to improve customer experience. We would like to see designs that use a black background. The final design should communicate sophistication and customer service, as well as stability and technology.

Industry/Entity Type

Real Estate

Requirements
Must have
• Black background

```html
<!DOCTYPE html>
<html lang="en">
<head>
<meta charset="utf-8">
<title>Orvantiq – Business Card</title>
<link rel="stylesheet" href="https://fonts.googleapis.com/css2?family=Exo+2:wght@400;600&display=swap">
<style>
  :root {
    --page-bg: #e4e2df;
    --card-black: #070707;
    --brand-blue: #8fb4e6;
    --accent-red: #d8243d;
    --edge-blue: #6f8fd0;
    --sky-top: #9cc0ea;
    --sky-bottom: #dfe6ee;
    --text-white: #ffffff;
  }
  * { box-sizing: border-box; margin: 0; padding: 0; }
  html, body {
    width: 1200px;
    height: 900px;
    overflow: hidden;
    background: var(--page-bg);
    font-family: "Exo 2", sans-serif;
  }
  .canvas {
    position: relative;
    width: 1200px;
    height: 900px;
  }
  .card {
    position: absolute;
    left: 320px;
    width: 560px;
    height: 320px;
    background: var(--card-black);
    overflow: hidden;
    box-shadow: 0 6px 18px rgba(0,0,0,0.25);
  }
  .card--front { top: 100px; }
  .card--back { top: 480px; }
  .card-shapes {
    position: absolute;
    inset: 0;
    width: 100%;
    height: 100%;
  }
  .wordmark {
    position: absolute;
    color: var(--brand-blue);
    font-weight: 400;
    letter-spacing: 0.1em;
    line-height: 1;
    white-space: nowrap;
  }
  .card--front .wordmark {
    left: 0;
    right: 0;
    top: 134px;
    text-align: center;
    font-size: 54px;
  }
  .card--back .wordmark {
    left: 30px;
    top: 150px;
    font-size: 21px;
  }
  .contact {
    position: absolute;
    left: 310px;
    top: 200px;
    color: var(--text-white);
    line-height: 1.15;
    white-space: nowrap;
  }
  .contact-name {
    font-size: 26px;
    font-weight: 600;
  }
  .contact-role {
    font-size: 16px;
    margin-bottom: 4px;
  }
  .contact-line {
    font-size: 16px;
  }
  .contact-label--blue { color: var(--brand-blue); }
</style>
</head>
<body>
<main class="canvas">
  <section class="card card--front" aria-label="Card front">
    <div class="wordmark">ORVANTIQ</div>
  </section>

  <section class="card card--back" aria-label="Card back">
    <svg class="card-shapes" viewBox="0 0 560 320" xmlns="http://www.w3.org/2000/svg">
      <defs>
        <linearGradient id="skyFill" x1="0" y1="0" x2="0.3" y2="1">
          <stop offset="0" stop-color="var(--sky-top)"/>
          <stop offset="1" stop-color="var(--sky-bottom)"/>
        </linearGradient>
      </defs>
      <polygon class="chevron-red" points="92,0 128,0 252,138 560,168 560,182 246,170" fill="var(--accent-red)"/>
      <polyline class="chevron-edge" points="92,0 246,170 560,182" fill="none" stroke="var(--edge-blue)" stroke-width="1.5"/>
      <polygon class="house-photo" role="img" aria-label="Photo of a modern multi-storey home against a blue sky" points="128,0 560,0 560,168 252,138" fill="url(#skyFill)"/>
    </svg>
    <div class="wordmark">ORVANTIQ</div>
    <div class="contact">
      <div class="contact-name">Daniel Reyes</div>
      <div class="contact-role">Broker</div>
      <div class="contact-line">Tel: 555.214.3087</div>
      <div class="contact-line"><span class="contact-label--blue">Fax:</span> 555.214.3090</div>
      <div class="contact-line"><span class="contact-label--blue">Web:</span> www.orvantiq-homes.com</div>
    </div>
  </section>
</main>
</body>
</html>
```